Project Lists Banner for HVAC ecommerce store

We want a banner that showcases our project list feature that will allow customers to create list of products that they can select and quickly order. this will be a middle of page banner. It will replace this banner - https://www.brightsnapclip.com/image/40872316
Font: Noto Sans
Size: 938x300 px
Color Options: #0059E, #00BBE3, #C6C8C7
Text:
Create lists of frequently purchased SKU's for fast ordering.
- Warehouse Inventory
- Complete Systems
- Large Projects
- And More...
"Sign In" is the call to action button. make button with non rounded (square) boarders.
We don't want a computer screen in banner nor a person. You can look at our competitors below for ideas.
Our staging server is lintvale7.com for reference
Our competitors:
https://www.hollowmarksupply.com/
https://www.tolvexo.com/
https://www.quibo.com/
https://www.vesko.com/index.html
Target Market(s)
HVAC, B2B
Industry/Entity Type
HVAC
Look and feel

```html
<!DOCTYPE html>
<html lang="en">
<head>
<meta charset="utf-8">
<title>Project Lists Banner</title>
<link rel="stylesheet" href="https://fonts.googleapis.com/css2?family=Noto+Sans:ital,wght@0,600;0,700;1,600;1,700&display=swap">
<style>
  :root {
    --page-bg: #e9e9e9;
    --brand-blue: #00bbe3;
    --brand-blue-text: #00b2de;
    --divider-grey: #e3e3e3;
    --white: #ffffff;
  }
  * { margin: 0; padding: 0; box-sizing: border-box; }
  html, body {
    width: 1200px;
    height: 657px;
    overflow: hidden;
    background: var(--page-bg);
    font-family: "Noto Sans", sans-serif;
  }
  .banner {
    position: absolute;
    left: 151px;
    top: 185px;
    width: 938px;
    height: 300px;
    transform: scale(0.957);
    transform-origin: 0 0;
    background: var(--white);
    box-shadow: 0 1px 3px rgba(0,0,0,0.12);
    overflow: hidden;
  }
  .banner__shapes {
    position: absolute;
    inset: 0;
  }
  .banner__headline {
    position: absolute;
    left: 47px;
    top: 52px;
    color: var(--white);
    font-style: italic;
    font-weight: 700;
    font-size: 36px;
    line-height: 46px;
    text-transform: uppercase;
    text-shadow: 2px 2px 2px rgba(0,60,90,0.45);
    letter-spacing: -0.2px;
  }
  .banner__headline .headline__emphasis {
    font-size: 44px;
    line-height: 54px;
  }
  .feature-list {
    position: absolute;
    right: 44px;
    top: 36px;
    list-style: none;
    text-align: right;
  }
  .feature-list__item {
    display: flex;
    align-items: center;
    justify-content: flex-end;
    height: 42px;
    color: var(--brand-blue-text);
    font-weight: 600;
    font-size: 23px;
    text-transform: uppercase;
  }
  .feature-list__icon {
    width: 30px;
    height: 30px;
    margin-left: 12px;
    flex: none;
  }
  .feature-list__more {
    font-style: italic;
    text-transform: none;
    padding-right: 42px;
  }
  .cta-button {
    position: absolute;
    left: 697px;
    top: 213px;
    width: 155px;
    height: 52px;
    display: flex;
    align-items: center;
    justify-content: center;
    background: var(--brand-blue);
    color: var(--white);
    font-weight: 700;
    font-size: 23px;
    text-decoration: none;
    border-radius: 0;
  }
</style>
</head>
<body>
  <section class="banner">
    <svg class="banner__shapes" width="938" height="300" viewBox="0 0 938 300" role="img" aria-label="Blue panel with faint scattered square pattern">
      <polygon points="474,0 494,0 636,300 616,300" fill="var(--divider-grey)"/>
      <polygon points="0,0 474,0 634,300 0,300" fill="var(--brand-blue)"/>
    </svg>

    <h2 class="banner__headline">
      Create lists of<br>
      frequently purchased<br>
      <span class="headline__emphasis">SKU's</span> for<br>
      fast ordering
    </h2>

    <ul class="feature-list">
      <li class="feature-list__item">Warehouse Inventory
        <svg class="feature-list__icon" viewBox="0 0 30 30" aria-hidden="true">
          <g fill="none" stroke="var(--brand-blue)" stroke-width="2.4">
            <rect x="6" y="2" width="18" height="7"/>
            <rect x="6" y="11" width="18" height="7"/>
          </g>
          <rect x="13.8" y="18" width="2.4" height="5" fill="var(--brand-blue)"/>
          <rect x="4" y="23" width="22" height="3" fill="var(--brand-blue)"/>
          <rect x="9" y="5" width="6" height="1.5" fill="var(--brand-blue)"/>
          <rect x="9" y="14" width="6" height="1.5" fill="var(--brand-blue)"/>
        </svg>
      </li>
      <li class="feature-list__item">Complete Systems
        <svg class="feature-list__icon" viewBox="0 0 30 30" aria-hidden="true">
          <path d="M4 14 V9 H22" fill="none" stroke="var(--brand-blue)" stroke-width="3.4"/>
          <polygon points="21,3 28,9 21,15" fill="var(--brand-blue)"/>
          <path d="M26 16 V21 H8" fill="none" stroke="var(--brand-blue)" stroke-width="3.4"/>
          <polygon points="9,15 2,21 9,27" fill="var(--brand-blue)"/>
        </svg>
      </li>
      <li class="feature-list__item">Large Projects
        <svg class="feature-list__icon" viewBox="0 0 30 30" aria-hidden="true">
          <rect x="11" y="3" width="8" height="8" fill="var(--brand-blue)"/>
          <path d="M15 11 V15 M5 19 V15 H25 V19 M15 15 V19" fill="none" stroke="var(--brand-blue)" stroke-width="1.6"/>
          <rect x="1" y="19" width="8" height="7" fill="var(--brand-blue)"/>
          <rect x="11" y="19" width="8" height="7" fill="var(--brand-blue)"/>
          <rect x="21" y="19" width="8" height="7" fill="var(--brand-blue)"/>
        </svg>
      </li>
      <li class="feature-list__item feature-list__more">And More...</li>
    </ul>

    <a class="cta-button" href="#">SIGN IN</a>
  </section>
</body>
</html>
```